Modern Design Business Card industrial maintenance company

Business card design for Company named Brookvale Equipment Services

Target Market(s)

Industrial

Industry/Entity Type

Maintenance and repair

Contact Information for Business Card

Place holder for address, office phone, mobile number and email

Requirements
Must have
• Clean modern look
Nice to have
• N/a

```html
<!DOCTYPE html>
<html lang="en">
<head>
<meta charset="utf-8">
<title>Brookvale Equipment Services – Business Card</title>
<link rel="stylesheet" href="https://fonts.googleapis.com/css2?family=Roboto:wght@400;700&display=swap">
<style>
  :root {
    --backdrop: #2b2b2b;
    --card-white: #ffffff;
    --card-black: #0d0d0d;
    --pattern-tone: #1a1a1a;
    --ink: #111111;
    --ink-soft: #6b6b6b;
    --ink-mid: #4a4a4a;
    --mark-white: #ffffff;
  }
  * { margin: 0; padding: 0; box-sizing: border-box; }
  html, body {
    width: 1200px; height: 900px; overflow: hidden;
    background: radial-gradient(circle at 50% 45%, #3a3a3a, var(--backdrop) 70%);
    font-family: "Roboto", sans-serif;
  }
  .stage {
    position: relative; width: 1200px; height: 900px;
    display: flex; justify-content: center; align-items: center; gap: 80px;
  }
  .card {
    position: relative; width: 370px; height: 640px;
    box-shadow: 0 20px 50px rgba(0,0,0,0.55);
    overflow: hidden;
  }
  /* Front */
  .card-front { background: var(--card-white); }
  .front-brand {
    position: absolute; top: 64px; left: 44px;
    display: flex; align-items: center; gap: 14px;
  }
  .brand-circle {
    width: 74px; height: 74px; border-radius: 50%;
    border: 6px solid var(--ink);
  }
  .brand-name {
    font-weight: 700; font-size: 24px; color: var(--ink); letter-spacing: 0.5px;
  }
  .front-details {
    position: absolute; right: 40px; bottom: 64px;
    text-align: right;
  }
  .person-name {
    font-weight: 700; font-size: 24px; letter-spacing: 1px;
    color: var(--ink); text-transform: uppercase;
  }
  .person-title {
    font-size: 17px; color: var(--ink-soft); margin-top: 4px; margin-bottom: 26px;
  }
  .company, .address { font-size: 17px; color: var(--ink-soft); line-height: 1.35; }
  .contact-list { list-style: none; margin-top: 22px; }
  .contact-list li {
    font-size: 17px; color: var(--ink-mid); line-height: 1.5;
    display: flex; justify-content: flex-end; align-items: center; gap: 8px;
  }
  .contact-list svg { width: 16px; height: 16px; flex: none; }
  .front-band {
    position: absolute; left: 0; bottom: 0; width: 46%; height: 14px;
    background: var(--card-black);
  }
  /* Back */
  .card-back { background: var(--card-black); }
  .back-pattern {
    position: absolute; inset: 22px;
    background: linear-gradient(160deg, #202020, var(--pattern-tone) 60%, #111);
    border-radius: 4px;
  }
  .back-brand {
    position: absolute; left: 50%; top: 62%; transform: translate(-50%, -50%);
    display: flex; flex-direction: column; align-items: center; gap: 12px;
  }
  .back-brand .brand-circle { border-color: var(--mark-white); width: 68px; height: 68px; border-width: 5px; }
  .back-brand .brand-name { color: var(--mark-white); font-size: 20px; }
</style>
</head>
<body>
<main class="stage">
  <section class="card card-front" aria-label="Card front">
    <div class="front-brand">
      <div class="brand-circle"></div>
      <span class="brand-name">Brookvale</span>
    </div>
    <div class="front-details">
      <h1 class="person-name">Daniel Hartwell</h1>
      <p class="person-title">Managing Director</p>
      <p class="company">Brookvale Equipment Services</p>
      <p class="address">218 W Orchard Rd<br>Lakemont, CA 91450</p>
      <ul class="contact-list">
        <li>(555) 310-4827
          <svg viewBox="0 0 16 16" aria-hidden="true"><circle cx="8" cy="8" r="8" fill="#111"/><path d="M5 4.5h2l.7 2-1.2.8a5 5 0 0 0 2.2 2.2l.8-1.2 2 .7v2A1 1 0 0 1 10.5 12 6.5 6.5 0 0 1 4 5.5a1 1 0 0 1 1-1z" fill="#fff"/></svg>
        </li>
        <li>info@brookvalees.com
          <svg viewBox="0 0 16 16" aria-hidden="true"><circle cx="8" cy="8" r="8" fill="#111"/><rect x="4" y="5" width="8" height="6" fill="#fff"/><path d="M4 5l4 3 4-3" stroke="#111" stroke-width="1" fill="none"/></svg>
        </li>
        <li>www.brookvalees.com
          <svg viewBox="0 0 16 16" aria-hidden="true"><circle cx="8" cy="8" r="8" fill="#111"/><circle cx="8" cy="8" r="4.5" fill="none" stroke="#fff"/><path d="M3.5 8h9M8 3.5c-2 2.5-2 6.5 0 9M8 3.5c2 2.5 2 6.5 0 9" stroke="#fff" fill="none" stroke-width="0.8"/></svg>
        </li>
      </ul>
    </div>
    <div class="front-band"></div>
  </section>

  <section class="card card-back" aria-label="Card back">
    <div class="back-pattern" role="img" aria-label="Repeated embossed brand mark pattern covering the card back"></div>
    <div class="back-brand">
      <div class="brand-circle"></div>
      <span class="brand-name">Brookvale</span>
    </div>
  </section>
</main>
</body>
</html>
```